We need a business card design for a Dubai based company .

We need a business card for a Dubai based company called "Zernova Smoking Requisites Trading LLC". We mainly import Flavoured Tobacco products and Charcoal which is used for smoking in a Hookah/Shisha and distribute to the wholesalers and retailers. Logo file is attached herewith.

```html
<!DOCTYPE html>
<html lang="en">
<head>
<meta charset="utf-8">
<title>Zernova Business Card</title>
<link rel="stylesheet" href="https://fonts.googleapis.com/css2?family=Montserrat:wght@400;500;600&display=swap">
<style>
  :root {
    --backdrop: #3b322e;
    --card: #1f1f20;
    --card-light: #2b2c2d;
    --red: #d3333a;
    --edge-red: #8e2a2c;
    --white: #f4f4f4;
  }
  * { box-sizing: border-box; margin: 0; padding: 0; }
  html, body {
    width: 1200px; height: 716px; overflow: hidden;
    background: var(--backdrop);
    font-family: "Montserrat", sans-serif;
  }
  .canvas {
    width: 1200px; height: 716px;
    display: flex; align-items: center; justify-content: center; gap: 50px;
  }
  .card {
    width: 540px; height: 310px;
    border-radius: 10px;
    background: linear-gradient(135deg, var(--card-light), var(--card) 60%);
    position: relative;
    box-shadow: 0 6px 0 var(--edge-red), 0 18px 30px rgba(0,0,0,.45);
  }
  .card--back { box-shadow: 0 18px 30px rgba(0,0,0,.45); }
  .company-name {
    position: absolute;
    color: var(--white);
    font-weight: 500;
    line-height: 1.35;
  }
  .card--front .company-name {
    left: 50%; top: 50%;
    transform: translate(-50%, -50%);
    width: 380px;
    font-size: 26px;
    text-align: center;
  }
  .card--back .company-name {
    left: 34px; top: 50%;
    transform: translateY(-50%);
    width: 240px;
    font-size: 19px;
  }
  .divider {
    position: absolute; left: 300px; top: 78px;
    width: 1px; height: 154px; background: var(--red);
  }
  .contact {
    position: absolute; left: 322px; top: 84px;
    color: var(--white);
    font-size: 12.5px; line-height: 1.5;
  }
  .contact__name {
    color: var(--red); font-weight: 600;
    font-size: 17px; letter-spacing: 1px; text-transform: uppercase;
  }
  .contact__role { text-transform: uppercase; letter-spacing: .8px; margin-bottom: 2px; }
  .contact__line { display: flex; align-items: center; gap: 6px; }
  .contact__line svg { width: 10px; height: 10px; flex-shrink: 0; }
</style>
</head>
<body>
<main class="canvas">
  <section class="card card--front">
    <p class="company-name">Zernova Smoking Requisites Trading LLC</p>
  </section>

  <section class="card card--back">
    <p class="company-name">Zernova Smoking Requisites Trading LLC</p>
    <div class="divider"></div>
    <div class="contact">
      <p class="contact__name">Daniel Brooks</p>
      <p class="contact__role">Director</p>
      <p>418 Harbor Lane,<br>Suite 12 Riverton, PA</p>
      <p class="contact__line">
        <svg viewBox="0 0 10 10"><path d="M2 1 L4 1 L4.5 3 L3.4 3.8 Q4.3 5.8 6.2 6.6 L7 5.5 L9 6 L9 8 Q5 9 1.5 4.5 Q1 2.5 2 1 Z" fill="var(--red)"/></svg>
        5550142287
      </p>
      <p class="contact__line">
        <svg viewBox="0 0 10 10"><rect x="0.7" y="2" width="8.6" height="6" fill="none" stroke="var(--red)" stroke-width="1"/><path d="M0.7 2 L5 5.5 L9.3 2" fill="none" stroke="var(--red)" stroke-width="1"/></svg>
        info@zernova.com
      </p>
      <p class="contact__line">
        <svg viewBox="0 0 10 10"><circle cx="5" cy="5" r="4.2" fill="none" stroke="var(--red)"/><ellipse cx="5" cy="5" rx="1.8" ry="4.2" fill="none" stroke="var(--red)" stroke-width=".8"/><path d="M0.8 5 H9.2" stroke="var(--red)" stroke-width=".8"/></svg>
        www.zernova.com
      </p>
    </div>
  </section>
</main>
</body>
</html>
```